| 希望する色 | 黄系 |
【 概要 】 PAKUのリッチの制作をお願いします。 ほぼデザインを出来ているのでデータへの落し込みと多少のブラッシュアップをお願い出来ればと思います。 【 依頼内容 】 添付した画像のように1枚の画像に6分割したリッチメニューになります。 ファイル形式:JPG、JPEG、PNG ファイルサイズ:1MB以下 画像サイズ:2500px × 1686px 【 提供素材 】 ・添付ファイルよりご確認下さい。 【 デザインイメージ 】 ・シンプル ・ピクトグラン ・こちらのサイトのPAKUアカウントで使用します https://morizuto.jp/ 良ければ友達追加をしてイメージ頂けますと幸いです。 <a href="https://tsu.ee/Q8pW2RZ"><img src="https://cdn.paku-assets.example/n/paku_add_friends/btn/ja.png" alt="友だち追加" height="36" border="0"></a> ご質問がありましたら、気軽にお問い合わせください。 応募をお待ちしております! |
| 参考記事URL | ||
| https://morizuto.jp/ | ||
どれも素敵なご提案を頂いたのですが一番動線を考えられた作品を選ばせて頂きました。
色々なご提案を頂いたのにお選び出来ずに申し訳ございません。
また色々と今後もお願いをする計画がございますのでぜひ次回もご参画を頂けますと幸いです。

```html
<!DOCTYPE html>
<html lang="ja">
<head>
<meta charset="utf-8">
<title>PAKU リッチメニュー</title>
<link rel="stylesheet" href="https://fonts.googleapis.com/css2?family=Noto+Sans+JP:wght@500;700&display=swap">
<style>
  :root {
    --bg: #ffffff;
    --frame-outer: #f2a900;
    --frame-inner: #ffd84a;
    --label: #fff100;
    --ink: #1a1a1a;
    --icon: #4b4b4b;
    --wave: #e0201b;
  }
  * { box-sizing: border-box; margin: 0; padding: 0; }
  html, body { width: 1200px; height: 810px; overflow: hidden; background: var(--bg); }
  .menu {
    position: relative;
    width: 1200px; height: 810px;
    display: grid;
    grid-template-columns: repeat(3, 390px);
    grid-template-rows: repeat(2, 396px);
    gap: 12px 15px;
    padding: 3px 0 0 3px;
    font-family: "Noto Sans JP", sans-serif;
  }
  .tile {
    position: relative;
    border: 4px solid var(--frame-outer);
    box-shadow: inset 0 0 0 5px var(--frame-inner);
    background: var(--bg);
  }
  .label {
    position: absolute;
    left: 50%; top: 42px;
    transform: translateX(-50%);
    background: var(--label);
    color: var(--ink);
    font-weight: 500;
    font-size: 31px;
    line-height: 1.45;
    letter-spacing: 0.04em;
    text-align: center;
    white-space: nowrap;
    padding: 4px 22px;
  }
  .label.two-line { top: 40px; padding: 4px 18px; }
  .wave {
    position: absolute;
    left: 50%; top: 104px;
    transform: translateX(-50%);
    width: 150px; height: 14px;
  }
  .icon {
    position: absolute;
    left: 50%;
    transform: translateX(-50%);
    fill: var(--icon);
  }
  .operator {
    position: absolute;
    left: 50%; top: 160px;
    transform: translateX(-50%);
    width: 150px; height: 170px;
    border-radius: 70px 70px 20px 20px;
    background: linear-gradient(#5a5a5a, #3f3f3f);
  }
  .icon-calendar { top: 158px; width: 190px; height: 180px; }
  .icon-form { top: 160px; width: 170px; height: 170px; }
  .icon-truck { top: 208px; width: 240px; height: 130px; }
  .icon-utilities { top: 150px; width: 290px; height: 200px; }
  .icon-key { top: 170px; width: 190px; height: 190px; }
</style>
</head>
<body>
<main class="menu">

  <section class="tile">
    <h2 class="label">モリズトする</h2>
    <svg class="wave" viewBox="0 0 150 14" aria-hidden="true">
      <path d="M0 7 q6 -7 12 0 t12 0 t12 0 t12 0 t12 0 t12 0 t12 0 t12 0 t12 0 t12 0 t12 0 t12 0 t6 0" fill="none" stroke="var(--wave)" stroke-width="3"/>
    </svg>
    <div class="operator" role="img" aria-label="ヘッドセットを着けたオペレーターのピクトグラム"></div>
  </section>

  <section class="tile">
    <h2 class="label">内見予約をする</h2>
    <svg class="icon icon-calendar" viewBox="0 0 190 180" aria-hidden="true">
      <rect x="5" y="22" width="180" height="155" rx="18"/>
      <rect x="20" y="62" width="150" height="100" fill="#fff"/>
      <rect x="40" y="4" width="18" height="40" rx="9" stroke="#fff" stroke-width="5"/>
      <rect x="132" y="4" width="18" height="40" rx="9" stroke="#fff" stroke-width="5"/>
      <g>
        <rect x="58" y="72" width="18" height="16"/><rect x="86" y="72" width="18" height="16"/><rect x="114" y="72" width="18" height="16"/><rect x="142" y="72" width="18" height="16"/>
        <rect x="30" y="98" width="18" height="16"/><rect x="58" y="98" width="18" height="16"/><rect x="86" y="98" width="18" height="16"/><rect x="142" y="98" width="18" height="16"/>
        <rect x="30" y="124" width="18" height="16"/><rect x="58" y="124" width="18" height="16"/><rect x="86" y="124" width="18" height="16"/><rect x="114" y="124" width="18" height="16"/>
      </g>
      <path d="M110 108 l10 10 l20 -24" fill="none" stroke="var(--icon)" stroke-width="7"/>
    </svg>
  </section>

  <section class="tile">
    <h2 class="label">申込みをする</h2>
    <svg class="icon icon-form" viewBox="0 0 170 170" aria-hidden="true">
      <rect x="12" y="18" width="120" height="145" rx="6" fill="none" stroke="var(--icon)" stroke-width="11"/>
      <rect x="38" y="52" width="55" height="9"/>
      <rect x="38" y="78" width="55" height="9"/>
      <rect x="38" y="104" width="42" height="9"/>
      <path d="M160 8 q-30 10 -55 55 l-18 40 l10 4 l22 -38 q30 -25 41 -61z"/>
      <rect x="36" y="136" width="62" height="8"/>
    </svg>
  </section>

  <section class="tile">
    <h2 class="label two-line">引越し業者の<br>手配をする</h2>
    <svg class="icon icon-truck" viewBox="0 0 240 130" aria-hidden="true">
      <rect x="60" y="0" width="178" height="92"/>
      <path d="M0 50 l10 -40 h44 v82 h-54z"/>
      <rect x="14" y="16" width="26" height="28" fill="#fff"/>
      <rect x="0" y="96" width="238" height="10"/>
      <circle cx="36" cy="108" r="20" stroke="#fff" stroke-width="5"/>
      <circle cx="190" cy="108" r="20" stroke="#fff" stroke-width="5"/>
    </svg>
  </section>

  <section class="tile">
    <h2 class="label two-line">ライフラインの<br>手配をする</h2>
    <svg class="icon icon-utilities" viewBox="0 0 290 200" aria-hidden="true">
      <!-- faucet -->
      <rect x="30" y="14" width="30" height="8" rx="3"/>
      <rect x="41" y="20" width="8" height="14"/>
      <path d="M4 34 h66 v24 h-30 v22 h-18 v-22 h-18z"/>
      <rect x="24" y="84" width="14" height="6"/>
      <!-- bulb -->
      <circle cx="132" cy="30" r="28"/>
      <rect x="118" y="54" width="28" height="22" rx="3"/>
      <rect x="124" y="78" width="16" height="8" rx="3"/>
      <!-- stove -->
      <path d="M198 22 q-6 -8 0 -16 q6 8 0 16z M226 22 q-6 -8 0 -16 q6 8 0 16z M254 22 q-6 -8 0 -16 q6 8 0 16z"/>
      <rect x="190" y="40" width="74" height="8"/>
      <rect x="190" y="48" width="6" height="18"/>
      <rect x="258" y="48" width="6" height="18"/>
      <rect x="186" y="64" width="90" height="6"/>
      <!-- phone -->
      <path d="M40 108 l14 -6 l14 26 l-12 8 q6 18 22 30 l10 -10 l24 16 l-6 14 q-40 2 -66 -78z"/>
      <!-- laptop -->
      <rect x="108" y="100" width="150" height="86" rx="6" fill="none" stroke="var(--icon)" stroke-width="9"/>
      <rect x="96" y="188" width="174" height="8" rx="3"/>
      <circle cx="183" cy="143" r="26" fill="none" stroke="var(--icon)" stroke-width="5"/>
      <ellipse cx="183" cy="143" rx="11" ry="26" fill="none" stroke="var(--icon)" stroke-width="4"/>
      <rect x="157" y="141" width="52" height="4"/>
      <rect x="162" y="128" width="42" height="3"/>
      <rect x="162" y="155" width="42" height="3"/>
    </svg>
  </section>

  <section class="tile">
    <h2 class="label two-line">鍵受渡方法を<br>確認する</h2>
    <svg class="icon icon-key" viewBox="0 0 190 190" aria-hidden="true">
      <g transform="rotate(40 95 95)">
        <rect x="18" y="60" width="70" height="70" rx="16"/>
        <rect x="40" y="78" width="26" height="12" rx="6" fill="#fff"/>
        <rect x="84" y="84" width="96" height="22" rx="4"/>
        <rect x="116" y="104" width="14" height="16"/>
        <rect x="140" y="104" width="14" height="22"/>
        <rect x="164" y="104" width="14" height="14"/>
      </g>
    </svg>
  </section>

</main>
</body>
</html>
```